Business Card

Company: Willow Ridge Nursery.

Use uploaded logo or design one just like it. This is a tree growing operation and really like earth tone colors.

Target Market(s)

Landscaping company's, retail nurseries, and landscape arc.

Industry/Entity Type

Business

Font styles to use
Serif

Requirements
Must have
• Name: Dale Whitford
Title: Owner
Address: 48217 W. 150 Road, Grove, OK 74592
Office: 918-555-3172
Cell: 918-555-6094
Fax: 918-555-4418
email: dalewr@plainsmail.net
Willow Ridge Nursery

```html
<!DOCTYPE html>
<html lang="en">
<head>
<meta charset="utf-8">
<title>Willow Ridge Nursery – Business Card</title>
<link rel="stylesheet" href="https://fonts.googleapis.com/css2?family=Tenor+Sans&display=swap">
<style>
  :root {
    --card-bg: #ffffff;
    --ink: #111111;
    --brand-green: #2f9a3c;
    --art-top: #e4ecdc;
    --art-bottom: #e8b070;
  }
  html, body {
    margin: 0;
    padding: 0;
    overflow: hidden;
    background: var(--card-bg);
  }
  .card {
    position: relative;
    width: 1200px;
    height: 686px;
    background: var(--card-bg);
    overflow: hidden;
    font-family: "Tenor Sans", sans-serif;
    font-variant: small-caps;
    color: var(--ink);
  }
  .card__art {
    position: absolute;
    left: 0;
    top: 12px;
    width: 415px;
    height: 396px;
    background: linear-gradient(180deg, var(--art-top) 0%, var(--art-bottom) 100%);
  }
  .card__company {
    position: absolute;
    left: 469px;
    width: 600px;
    top: 40px;
    margin: 0;
    text-align: center;
    font-size: 34px;
    line-height: 50px;
    font-weight: 400;
    letter-spacing: 0.24em;
    color: var(--brand-green);
  }
  .card__block {
    position: absolute;
    left: 342px;
    width: 900px;
    margin: 0;
    text-align: center;
    font-size: 40px;
    line-height: 50px;
    letter-spacing: 0.2em;
  }
  .person  { top: 138px; }
  .address { top: 280px; line-height: 46px; }
  .phones  { top: 420px; }
  .email   { top: 613px; }
</style>
</head>
<body>
  <main class="card">
    <div class="card__art" role="img" aria-label="Nursery artwork: a young tree and soil"></div>

    <h1 class="card__company">Willow Ridge Nursery</h1>

    <p class="card__block person">Owner<br>Dale Whitford</p>
    <p class="card__block address">Address: 48217 W. 150 Road,<br>Grove, OK 74592</p>
    <p class="card__block phones">Office: 918-555-3172<br>Cell: 918-555-6094<br>Fax: 918-555-4418</p>
    <p class="card__block email">email: dalewr@plainsmail.net</p>
  </main>
</body>
</html>
```